CD Cover Art for Breakout Album

I'm looking for cover art for my album that is in the "Americana" genre. It has some songs that are a little towards hard rock, but a couple are softer ballads as well. The album is called "Lanterns, Orchards, and Harvests," focusing on the after-effects of combat on the ones that serve. I want to integrate red, white and blue themes that are not pandering or kitchy. If possible, I would like to subtly integrate the "battlefield cross" which is attached as an image. I would like it to be as simple as possible, and don't want it solely military focused because the album is a collection of stories, only a few of which are explicitly military.

```html
<!DOCTYPE html>
<html lang="en">
<head>
<meta charset="UTF-8">
<title>Lanterns, Orchards, and Harvests — Album Cover</title>
<link href="https://fonts.googleapis.com/css2?family=Anton&display=swap" rel="stylesheet">
<style>
  :root {
    --navy-deep: #0b1a2e;
    --navy: #16365a;
    --steel-blue: #3f7fb4;
    --sky-blue: #9cc6e6;
    --mist-white: #e9eef0;
    --flag-red: #d41c14;
    --ember-red: #b8170f;
    --ground: #0a0f16;
    --title-white: #ffffff;
  }
  html, body {
    margin: 0;
    padding: 0;
    width: 1200px;
    height: 1200px;
    overflow: hidden;
    background: var(--navy-deep);
  }
  .album-cover {
    position: relative;
    width: 1200px;
    height: 1200px;
    overflow: hidden;
  }
  .cover-artwork {
    position: absolute;
    inset: 0;
    background:
      linear-gradient(180deg, rgba(11,26,46,0) 0%, rgba(11,26,46,0) 82%, var(--ground) 100%),
      linear-gradient(90deg,
        var(--navy-deep) 0%,
        var(--navy) 12%,
        var(--steel-blue) 28%,
        var(--sky-blue) 38%,
        var(--ember-red) 45%,
        var(--flag-red) 52%,
        var(--mist-white) 59%,
        var(--flag-red) 67%,
        var(--ember-red) 74%,
        var(--sky-blue) 82%,
        var(--steel-blue) 90%,
        var(--navy) 100%);
  }
  .cover-title {
    position: absolute;
    inset: 0;
    width: 1200px;
    height: 1200px;
  }
  .cover-title__line {
    font-family: "Anton", "Impact", sans-serif;
    font-size: 172px;
    fill: var(--title-white);
    text-transform: uppercase;
  }
</style>
</head>
<body>
  <main class="album-cover">
    <div class="cover-artwork" role="img" aria-label="Painted scene of tall red, white and blue vertical streaks like a weathered flag, with the silhouette of a kneeling figure beside a battlefield cross on dark grass at the bottom"></div>

    <svg class="cover-title" viewBox="0 0 1200 1200" xmlns="http://www.w3.org/2000/svg" aria-label="Lanterns, Orchards, and Harvests">
      <text class="cover-title__line" transform="translate(152 1212) rotate(-90)" textLength="1230" lengthAdjust="spacingAndGlyphs">Lanterns, Orchards,</text>
      <text class="cover-title__line" transform="translate(354 1212) rotate(-90)" textLength="1010" lengthAdjust="spacingAndGlyphs">and Harvests</text>
    </svg>
  </main>
</body>
</html>
```